Garnett and Lyle Personal Injury Billboard

We'd like a clean/modern billboard to build brand awareness for our law firm in the area of personal injury. Ideally, we like the word "Injured?" or something similar in large lettering.

I'm attaching images, logo and award badges which could be used. The billboards will be 14x48 ft and 10.6x36.

We are open to different color ideas, fonts, and artwork. Creative but not too busy with wording. Our web page is www.kgarnettfirm.example

Garnett & Lyle Law Firm
(555) 318-4092

```html
<!DOCTYPE html>
<html lang="en">
<head>
<meta charset="utf-8">
<title>Garnett and Lyle Personal Injury Billboard</title>
<link rel="stylesheet" href="https://fonts.googleapis.com/css2?family=Montserrat:wght@400;700;800&display=swap">
<style>
  :root {
    --stage: #858585;
    --brand-blue: #0177d2;
    --ink: #000000;
    --paper: #ffffff;
    --photo-light: #8a8580;
    --photo-dark: #4f4c4a;
    --badge-fill: #4fb0e8;
    --badge-edge: #dff1fb;
  }
  html, body {
    margin: 0;
    padding: 0;
    width: 1200px;
    height: 1154px;
    overflow: hidden;
    background: var(--stage);
  }
  .board-stage {
    position: relative;
    width: 1200px;
    height: 1154px;
  }
  .billboard {
    position: absolute;
    left: 41px;
    top: 412px;
    width: 1113px;
    height: 325px;
    font-family: "Montserrat", Arial, sans-serif;
  }
  .board-shadow {
    position: absolute;
    left: 120px;
    top: 725px;
    width: 960px;
    height: 22px;
    border-radius: 50%;
    background: rgba(0, 0, 0, 0.45);
    filter: blur(8px);
  }
  .billboard svg { display: block; width: 100%; height: 100%; }
  .headline { font-weight: 800; fill: var(--brand-blue); }
  .subline { font-weight: 400; fill: var(--ink); }
  .phone { font-weight: 800; fill: var(--ink); }
  .web { font-weight: 800; fill: var(--paper); }
  .firm-name { font-weight: 700; fill: var(--ink); }
</style>
</head>
<body>
<main class="board-stage">
  <div class="board-shadow"></div>
  <section class="billboard">
    <svg viewBox="0 0 1818 531" xmlns="http://www.w3.org/2000/svg">
      <defs>
        <linearGradient id="attorney-tone" x1="0" y1="0" x2="0" y2="1">
          <stop offset="0" stop-color="var(--photo-light)"/>
          <stop offset="1" stop-color="var(--photo-dark)"/>
        </linearGradient>
      </defs>

      <rect class="field" width="1818" height="531" fill="var(--brand-blue)"/>

      <rect class="attorney-photo" role="img" aria-label="Photo of the two attorneys in suits, smiling"
            x="0" y="100" width="540" height="431" fill="url(#attorney-tone)"/>

      <polygon class="divider-left" points="637,0 654,0 480,531 463,531" fill="var(--ink)"/>
      <polygon class="message-panel" points="654,0 1674,0 1502,531 480,531" fill="var(--paper)"/>
      <polygon class="divider-right" points="1674,0 1692,0 1520,531 1502,531" fill="var(--ink)"/>

      <g class="firm-lockup">
        <text class="firm-name" x="1068" y="78" font-size="36" text-anchor="middle" letter-spacing="1">GARNETT &amp; LYLE</text>
        <text class="firm-name" x="1068" y="122" font-size="20" text-anchor="middle" letter-spacing="6">LAW FIRM</text>
      </g>

      <text class="headline" x="1070" y="255" font-size="104" text-anchor="middle" letter-spacing="1">INJURED?</text>
      <text class="subline" x="1072" y="302" font-size="34" text-anchor="middle">FREE CASE EVALUATION</text>
      <text class="phone" x="1072" y="372" font-size="60" text-anchor="middle">(555) 318-4092</text>

      <polygon class="web-bar" points="554,410 1540,410 1512,490 526,490" fill="var(--ink)"/>
      <text class="web" x="1014" y="465" font-size="46" text-anchor="middle">www.kgarnettfirm.example</text>

      <rect class="award-badge" role="img" aria-label="Community choice award winner badge"
            x="1618" y="276" width="153" height="214" fill="var(--badge-fill)" stroke="var(--badge-edge)" stroke-width="3"/>
    </svg>
  </section>
</main>
</body>
</html>
```